Stylish Business Card for Modern hair salon

I need a simple business card design using our salon logo and colours that are in the logo. We service clients of all ages but predominantly those in the 18 to 55 age range. We have a young staff and are looking to have a card that will present a modern and clean image that represents who we are. The card should be in black and white same as our logo. Minimal use of other colours is allowed.

Industry/Entity Type

Hair And Beauty

Contact Information for Business Card

The design should have the following information
salon name - TR Hair Studio
address - 2751 Birchfield Rd.E. Mississauga, ON L7P3K2
phone - 905 614-2870
website - trhairexample.ca
instagram - tr.hairstudio
twitter - @TR_HairStudio

Colors
000000
ffffff
474747

Requirements
Must have
• simple design, salon name, address, phone, website, instagram, twitter info
• Back of card should have the following:
• YOUR NEXT APPOINTMENT
• DATE
• TIME
Nice to have
• simple design, clear to see and read,
• predominantly black and white colour, minimal use of other colours is ok
Should not have
• many colours, various fonts

```html
<!DOCTYPE html>
<html lang="en">
<head>
<meta charset="utf-8">
<title>TR Hair Studio – Business Card</title>
<link rel="stylesheet" href="https://fonts.googleapis.com/css2?family=Lato:wght@400;700;900&display=swap">
<style>
:root{
  --black:#000000;
  --card:#0b0b0b;
  --white:#ffffff;
  --grey:#474747;
  --grey-dark:#2c2c2c;
  --grey-text:#5c5c5c;
  --stage:#e9e9e9;
}
*{box-sizing:border-box;margin:0;padding:0}
html,body{width:1200px;height:1200px;overflow:hidden;background:var(--stage)}
body{font-family:"Lato",sans-serif;color:var(--white)}
.sheet{position:relative;width:1200px;height:1200px}
.card{position:absolute;left:100px;width:1000px;height:571px;background:var(--card);overflow:hidden;box-shadow:0 10px 30px rgba(0,0,0,.35)}
.card--front{top:20px}
.card--back{top:609px}
.brand{display:flex;align-items:center;gap:14px;font-weight:900;letter-spacing:.04em;color:var(--white)}
.brand__mark{width:14px;height:14px;background:var(--white)}
.card--front .brand{position:absolute;left:70px;top:70px;font-size:64px}
.salon-name{position:absolute;left:70px;top:180px;font-size:50px;font-weight:700;letter-spacing:.02em}
.band{position:absolute;left:0}
.band--info{top:300px;width:700px;height:120px;background:var(--grey-dark)}
.band--contact{top:420px;width:700px;height:100px;background:var(--grey)}
.detail{position:absolute;display:flex;align-items:flex-start;gap:10px;font-size:21px;font-weight:700;line-height:1.15}
.detail svg{flex:none;margin-top:3px}
.dot{flex:none;width:16px;height:16px;margin-top:4px;border-radius:50%;background:var(--white)}
.photo{position:absolute;right:0;top:0;width:360px;height:520px;background:radial-gradient(ellipse at 45% 40%,#cfcfcf 0%,#6a6a6a 35%,#141414 75%)}
.card--back .brand{position:absolute;left:0;right:0;top:60px;justify-content:center;font-size:84px}
.appointment{position:absolute;left:0;right:0;top:210px;text-align:center;font-size:58px;font-weight:900;letter-spacing:.03em}
.field{position:absolute;font-size:30px;color:var(--grey-text);letter-spacing:.04em}
.field--date{left:150px;top:310px}
.field--time{right:150px;top:310px}
.card--back .band--contact{top:400px;width:1000px;height:130px}
</style>
</head>
<body>
<main class="sheet">
  <section class="card card--front" aria-label="Business card front">
    <div class="brand"><span>TR HAIR</span></div>
    <h1 class="salon-name">TR Hair Studio</h1>
    <div class="photo" role="img" aria-label="Black and white photograph of a woman with a sleek bob haircut seen from behind"></div>
    <div class="band band--info"></div>
    <div class="band band--contact"></div>
    <p class="detail" style="left:70px;top:318px">
      <svg width="16" height="22" viewBox="0 0 16 22"><path d="M8 0a8 8 0 0 0-8 8c0 6 8 14 8 14s8-8 8-14a8 8 0 0 0-8-8zm0 11a3 3 0 1 1 0-6 3 3 0 0 1 0 6z" fill="#fff"/></svg>
      <span>2751 Birchfield Rd.E. Mississauga,<br>ON L7P3K2</span>
    </p>
    <p class="detail" style="left:420px;top:318px"><span class="dot"></span><span>tr.hairstudio</span></p>
    <p class="detail" style="left:420px;top:354px"><span class="dot"></span><span>@TR_HairStudio</span></p>
    <p class="detail" style="left:70px;top:436px">
      <svg width="18" height="18" viewBox="0 0 24 24"><path d="M6.6 10.8a15 15 0 0 0 6.6 6.6l2.2-2.2a1 1 0 0 1 1-.25 11.4 11.4 0 0 0 3.6.57 1 1 0 0 1 1 1V20a1 1 0 0 1-1 1A17 17 0 0 1 3 4a1 1 0 0 1 1-1h3.5a1 1 0 0 1 1 1c0 1.25.2 2.45.57 3.6a1 1 0 0 1-.25 1z" fill="#fff"/></svg>
      <span>905 614-2870</span>
    </p>
    <p class="detail" style="left:70px;top:472px"><span class="dot"></span><span>trhairexample.ca</span></p>
  </section>

  <section class="card card--back" aria-label="Business card back">
    <div class="brand"><span>TR HAIR</span></div>
    <h2 class="appointment">YOUR NEXT APPOINTMENT</h2>
    <p class="field field--date">DATE: XX-XX-XXXX</p>
    <p class="field field--time">TIME: 00:00</p>
    <div class="band band--contact"></div>
    <p class="detail" style="left:50px;top:440px">
      <svg width="16" height="22" viewBox="0 0 16 22"><path d="M8 0a8 8 0 0 0-8 8c0 6 8 14 8 14s8-8 8-14a8 8 0 0 0-8-8zm0 11a3 3 0 1 1 0-6 3 3 0 0 1 0 6z" fill="#fff"/></svg>
      <span>2751 Birchfield Rd.E. Mississauga,<br>ON L7P3K2</span>
    </p>
    <p class="detail" style="left:460px;top:430px">
      <svg width="18" height="18" viewBox="0 0 24 24"><path d="M6.6 10.8a15 15 0 0 0 6.6 6.6l2.2-2.2a1 1 0 0 1 1-.25 11.4 11.4 0 0 0 3.6.57 1 1 0 0 1 1 1V20a1 1 0 0 1-1 1A17 17 0 0 1 3 4a1 1 0 0 1 1-1h3.5a1 1 0 0 1 1 1c0 1.25.2 2.45.57 3.6a1 1 0 0 1-.25 1z" fill="#fff"/></svg>
      <span>905 614-2870</span>
    </p>
    <p class="detail" style="left:460px;top:468px"><span class="dot"></span><span>trhairexample.ca</span></p>
    <p class="detail" style="left:740px;top:430px"><span class="dot"></span><span>tr.hairstudio</span></p>
    <p class="detail" style="left:740px;top:468px"><span class="dot"></span><span>@TR_HairStudio</span></p>
  </section>
</main>
</body>
</html>
```